Business Card for Multi-Brand Sportswear Company

We are looking for a business card which represents our company and the multiple brands within it.

The company: Kelt Athletic (LTD)
The brands: Kelt, PawaLuni, VerdantFlex, Grit and Gale

Employees using these cards would be representing Kelt Athletic, rather than any of the individual brands. You will see a current design within the uploaded files, to give some inspiration. The actual text of the brands is not necessary, but the logos should be on there is some format.

Our creative minds on this are stretched, so we are looking for someone to make this their own, and show us what a good business card should look like.

We may like to get these printed with spot gloss, so keep that in mind with your designs.

www.keltathletic.co.uk

Industry/Entity Type

Business

Contact Information for Business Card

Tom Hollingsworth-Pryce
Operations Manager
(+44) 1632 960 418
Tom@keltathletic.co.uk
www.keltathletic.co.uk

Font styles to use
Sans Serif
Other font styles liked:
• Eurostile

Colors
ffffff

Requirements
Nice to have
• Dark (black) background

```html
<!DOCTYPE html>
<html lang="en">
<head>
<meta charset="utf-8">
<title>Kelt Athletic – Business Card</title>
<link href="https://fonts.googleapis.com/css2?family=Saira:wght@400;600;700&display=swap" rel="stylesheet">
<style>
  :root {
    --backdrop: #24252a;
    --card: #000000;
    --accent: #e8202a;
    --ink: #ffffff;
    --ink-soft: #d9d9d9;
  }
  * { margin: 0; padding: 0; box-sizing: border-box; }
  html, body {
    width: 1200px; height: 900px; overflow: hidden;
    background: var(--backdrop);
    font-family: "Saira", sans-serif;
    color: var(--ink);
  }
  .card {
    position: absolute;
    left: 280px;
    width: 640px; height: 366px;
    background: var(--card);
    overflow: hidden;
    box-shadow: 0 10px 30px rgba(0,0,0,.45);
  }
  .card--contact { top: 60px; }
  .card--brand { top: 474px; }
  .bands { position: absolute; inset: 0; width: 100%; height: 100%; }
  .bands polygon { fill: var(--accent); }

  /* contact side */
  .company-mark {
    position: absolute; top: 30px; left: 420px;
    font-weight: 600; font-size: 24px; letter-spacing: 1px;
    text-transform: uppercase; line-height: 1;
  }
  .person { position: absolute; left: 50px; top: 116px; }
  .person__name {
    font-weight: 700; font-size: 19px; letter-spacing: .5px;
    text-transform: uppercase;
  }
  .person__role {
    font-weight: 400; font-size: 17px; letter-spacing: 1.5px;
    text-transform: uppercase; color: var(--ink-soft); margin-top: 2px;
  }
  .contact-list {
    position: absolute; left: 400px; top: 92px;
    list-style: none; font-size: 13px; letter-spacing: .6px;
  }
  .contact-list li { display: flex; align-items: center; gap: 12px; height: 30px; }
  .contact-list svg { width: 18px; height: 18px; fill: none; stroke: var(--ink); stroke-width: 1.6; }
  .contact-list .icon-phone { fill: var(--ink); stroke: none; }
  .brand-row {
    position: absolute; left: 200px; right: 40px; bottom: 40px;
    display: flex; align-items: center; justify-content: space-between;
    font-weight: 600; font-size: 14px; letter-spacing: 1px; text-transform: uppercase;
  }
  .brand-row__item { display: flex; align-items: center; gap: 7px; }
  .dot-circle { width: 14px; height: 14px; border: 2px solid var(--ink); border-radius: 50%; }
  .dot-square { width: 14px; height: 14px; background: var(--ink); border-radius: 2px; }

  /* brand side */
  .hero-mark {
    position: absolute; left: 0; right: 0; top: 128px;
    text-align: center;
    font-weight: 700; font-size: 54px; letter-spacing: 3px;
    text-transform: uppercase; line-height: 1;
  }
  .hero-url {
    position: absolute; right: 40px; top: 232px;
    font-size: 22px; letter-spacing: 1px;
  }
</style>
</head>
<body>

<section class="card card--contact" aria-label="Business card, contact side">
  <svg class="bands" viewBox="0 0 640 366" aria-hidden="true">
    <polygon points="0,64 372,64 360,80 0,80"/>
    <polygon points="430,232 640,232 640,248 418,248"/>
  </svg>

  <div class="company-mark">Kelt Athletic</div>

  <div class="person">
    <p class="person__name">Tom Hollingsworth-Pryce</p>
    <p class="person__role">Operations Manager</p>
  </div>

  <ul class="contact-list">
    <li>
      <svg class="icon-phone" viewBox="0 0 24 24"><path d="M6.6 10.8a15 15 0 0 0 6.6 6.6l2.2-2.2a1 1 0 0 1 1-.25 11.4 11.4 0 0 0 3.6.6 1 1 0 0 1 1 1V20a1 1 0 0 1-1 1A17 17 0 0 1 3 4a1 1 0 0 1 1-1h3.5a1 1 0 0 1 1 1c0 1.25.2 2.45.6 3.6a1 1 0 0 1-.25 1z"/></svg>
      <span>(+44) 1632 960 418</span>
    </li>
    <li>
      <svg viewBox="0 0 24 24"><rect x="3" y="6" width="18" height="12"/><path d="M3 6l9 7 9-7"/></svg>
      <span>Tom@keltathletic.co.uk</span>
    </li>
    <li>
      <svg viewBox="0 0 24 24"><circle cx="12" cy="12" r="9"/><ellipse cx="12" cy="12" rx="4" ry="9"/><path d="M3 12h18"/></svg>
      <span>www.keltathletic.co.uk</span>
    </li>
  </ul>

  <div class="brand-row" aria-label="Group brands">
    <span class="brand-row__item">Kelt</span>
    <span class="brand-row__item">Grit and Gale</span>
    <span class="brand-row__item"><span class="dot-circle"></span>VerdantFlex</span>
    <span class="brand-row__item"><span class="dot-square"></span>PawaLuni</span>
  </div>
</section>

<section class="card card--brand" aria-label="Business card, brand side">
  <svg class="bands" viewBox="0 0 640 366" aria-hidden="true">
    <polygon points="262,40 640,40 640,56 250,56"/>
    <polygon points="0,306 372,306 360,322 0,322"/>
  </svg>
  <div class="hero-mark">Kelt Athletic</div>
  <div class="hero-url">www.keltathletic.co.uk</div>
</section>

</body>
</html>
```